Aviation Maintenance Business Card Design Challenge

We are seeking a compelling and professional business card design for the owner of a newly established company, Harrow Aerotech, LLC, based out of QMTB – Dunmore County Airport (Tolland Field) in Lawrenceville, Georgia. The company specializes in aircraft maintenance and detailing services, providing top-tier care and precision to both private and corporate aircraft owners. This business card will represent the owner, founder and operator, a licensed A&P (Airframe and Powerplant) Mechanic with over 20 years of hands-on aviation maintenance experience. His reputation is built on technical expertise, reliability, and a commitment to excellence — qualities that Harrow Aerotech aims to reflect in every aspect of its brand, including its visual identity.

Designers are encouraged to include elements such as the QMTB airport code, contact info layout suitable for mobile and field-based communication, and company branding that balances technical skill with personalized service.

Target Market(s)

Aircraft owners and operators

Industry/Entity Type

Aviation

Contact Information for Business Card

Name: Ed Marcus Whitby, (555) 314-2290, harrowaerotechllc@mailbox.example, www.harrowaerotech.example, QMTB – Dunmore County Airport (Tolland Field) Ashbury, Westmark 00000

Requirements
Must have
• Aeronautical themes or visual cues, highlight the company’s dual services: maintenance and cleaning/detailing, emphasize the owner's credentials, experience, and role as the face of the business
Nice to have
• Company logo

```html
<!DOCTYPE html>
<html lang="en">
<head>
<meta charset="utf-8">
<title>Harrow Aerotech, LLC — Business Card</title>
<link rel="stylesheet" href="https://fonts.googleapis.com/css2?family=Montserrat:ital,wght@0,300;0,400;0,700;1,300;1,400&display=swap">
<style>
  :root {
    --stage: #bdbec0;
    --card: #f3f3f5;
    --navy: #2e3192;
    --sky: #22c2ea;
    --sky-soft: #7fcbea;
    --icon-blue: #344e9a;
    --ink: #111111;
    --ink-soft: #222222;
    --rule: #9a9a9a;
    --white: #ffffff;
  }
  * { margin: 0; padding: 0; box-sizing: border-box; }
  html, body {
    width: 1200px; height: 1200px; overflow: hidden;
    background: var(--stage);
    font-family: "Montserrat", sans-serif;
  }
  .canvas { position: relative; width: 1200px; height: 1200px; }
  .card {
    position: absolute; left: 209px; width: 781px; height: 469px;
    background: var(--card); overflow: hidden;
  }
  .card--front { top: 60px; }
  .card--back { top: 674px; }
  .card svg.art { position: absolute; inset: 0; }
  .brand-mark {
    position: absolute; text-align: center; color: var(--navy);
    font-weight: 700; white-space: nowrap; line-height: 1.2;
  }
  .brand-mark__dot {
    display: inline-block; border-radius: 50%; background: var(--sky-soft);
    vertical-align: middle;
  }
  .brand-mark__tagline { display: block; font-weight: 400; }
  .card--front .brand-mark { left: 221px; top: 62px; transform: translateX(-50%); font-size: 20px; }
  .card--front .brand-mark__dot { width: 14px; height: 14px; margin-right: 6px; }
  .card--front .brand-mark__tagline { font-size: 9px; margin-top: 18px; }
  .card--back .brand-mark { left: 391px; top: 132px; transform: translateX(-50%); font-size: 40px; }
  .card--back .brand-mark__dot { width: 28px; height: 28px; margin-right: 12px; }
  .card--back .brand-mark__tagline { font-size: 15px; margin-top: 13px; }

  .company { position: absolute; color: var(--navy); font-weight: 700; white-space: nowrap; }
  .card--front .company { left: 52px; top: 138px; font-size: 29px; }
  .card--back .company { left: 221px; top: 250px; font-size: 29px; }

  .person { position: absolute; left: 52px; top: 200px; }
  .person__name { font-size: 30px; font-weight: 400; color: var(--ink); line-height: 1.15; }
  .person__role {
    display: inline-block; font-size: 22px; font-weight: 300; color: var(--ink);
    padding-bottom: 4px; border-bottom: 1px solid var(--rule); width: 172px; line-height: 1.3;
  }

  .contacts { position: absolute; left: 52px; top: 294px; list-style: none; }
  .contacts li {
    display: flex; align-items: center; gap: 13px;
    font-style: italic; font-weight: 300; font-size: 17.5px; color: var(--ink-soft);
    height: 26px;
  }
  .contacts li.contacts__address { height: 44px; line-height: 21px; margin-top: 2px; }
  .contacts svg { width: 15px; height: 15px; flex: none; }

  .services { position: absolute; font-weight: 300; line-height: 21px; }
  .services strong { font-weight: 700; }
  .card--front .services { left: 447px; top: 51px; font-size: 17.5px; color: var(--white); }
  .card--back .services { left: 221px; top: 356px; font-size: 17.4px; color: var(--ink); font-weight: 400; }
</style>
</head>
<body>
<main class="canvas">

  <section class="card card--front">
    <svg class="art" width="781" height="469" viewBox="0 0 781 469">
      <path fill="var(--sky-soft)" d="M337,0 C415,60 438,130 438,176 C438,215 418,250 396,278 C510,300 600,375 650,469 L781,469 L781,0 Z"/>
      <path fill="var(--sky)" d="M355,0 C430,60 455,130 455,176 C455,215 435,250 414,276 C520,296 610,370 665,469 L781,469 L781,0 Z"/>
      <g role="img" aria-label="Aircraft silhouette illustration">
        <rect x="515" y="152" width="100" height="96" rx="20" fill="var(--icon-blue)" opacity="0.85"/>
      </g>
      <g role="img" aria-label="Tools and jet badge illustration">
        <circle cx="643" cy="312" r="51" fill="none" stroke="var(--icon-blue)" stroke-width="3"/>
        <circle cx="643" cy="312" r="36" fill="var(--icon-blue)" opacity="0.85"/>
      </g>
    </svg>

    <div class="brand-mark">
      <span class="brand-mark__dot"></span>Harrow Aerotech
      <span class="brand-mark__tagline">Precision Above Every Horizon</span>
    </div>

    <h1 class="company">Harrow Aerotech, LLC</h1>

    <div class="person">
      <p class="person__name">Ed Marcus Whitby</p>
      <p class="person__role">A&amp;P Mechanic</p>
    </div>

    <ul class="contacts">
      <li>
        <svg viewBox="0 0 16 16"><rect width="16" height="16" fill="var(--sky-soft)"/><path d="M4 3 L6.5 3 L7.5 6 L6 7 C6.8 8.8 7.2 9.2 9 10 L10 8.5 L13 9.5 L13 12 C8 12.5 3.5 8 4 3 Z" fill="var(--navy)"/></svg>
        (555) 314-2290
      </li>
      <li>
        <svg viewBox="0 0 16 16"><rect width="16" height="16" fill="var(--sky-soft)"/><rect x="3" y="4.5" width="10" height="7" fill="var(--navy)"/><path d="M3 4.5 L8 8.5 L13 4.5" stroke="var(--sky-soft)" fill="none" stroke-width="1"/></svg>
        harrowaerotechllc@mailbox.example
      </li>
      <li>
        <svg viewBox="0 0 16 16"><rect width="16" height="16" fill="var(--sky-soft)"/><g fill="none" stroke="var(--navy)" stroke-width="1"><circle cx="8" cy="8" r="5"/><ellipse cx="8" cy="8" rx="2.2" ry="5"/><path d="M3 8 H13 M4 5.5 H12 M4 10.5 H12"/></g></svg>
        www.harrowaerotech.example
      </li>
      <li class="contacts__address">
        <svg viewBox="0 0 16 16"><rect width="16" height="16" fill="var(--sky-soft)"/><circle cx="8" cy="6.5" r="3" fill="none" stroke="var(--navy)" stroke-width="1.6"/><path d="M8 9.5 L8 13 M5 13 H11" stroke="var(--navy)" stroke-width="1.6"/></svg>
        <span>QMTB – Dunmore County Airport<br>(Tolland Field) Ashbury, Westmark 00000</span>
      </li>
    </ul>

    <p class="services"><strong>Services:</strong> Aircraft Maintenance &amp;<br>Detailing 20 Years of Experience<br>Trust, Reliability, and Expertise</p>
  </section>

  <section class="card card--back">
    <svg class="art" width="781" height="469" viewBox="0 0 781 469">
      <defs>
        <linearGradient id="stripeTone" x1="0" y1="0" x2="1" y2="1">
          <stop offset="0" stop-color="#ebebf0"/>
          <stop offset="0.5" stop-color="#f3f3f5"/>
          <stop offset="1" stop-color="#ebebf0"/>
        </linearGradient>
      </defs>
      <rect role="img" aria-label="Faint diagonal stripe pattern" width="781" height="469" fill="url(#stripeTone)"/>
    </svg>

    <div class="brand-mark">
      <span class="brand-mark__dot"></span>Harrow Aerotech
      <span class="brand-mark__tagline">Precision Above Every Horizon</span>
    </div>

    <h2 class="company">Harrow Aerotech, LLC</h2>

    <p class="services"><strong>Services:</strong> Aircraft Maintenance &amp; Detailing<br>20 Years of Experience<br>Trust, Reliability, and Expertise</p>
  </section>

</main>
</body>
</html>
```